International Health Supplement Company Needs Packaging and Label Redesign

Copperfield Vitals LLC requires a redesign for 1 internationally sold product and accompanying designs for 5 additional products. The additional products are currently sold locally and yet to be released internationally.

Our company is honest, premium, and passionate about supplements. We adopt a 'no BS' stance and as such source only the finest ingredients and deliver high-quality liquid health supplements to customers globally. We do not compromise on quality and do not apologise for price.

We want a clean, crisp design that conveys ‘premium, cutting-edge, boutique’ at a glance. We feel our current design appeals more to the 'chest beaters' rather than the 'chess players' that our research has indicated are our customers.

We have SIX PRODUCTS TOTAL in our range and feel individual color cues to distinguish the different products would greatly assist customer navigation i.e. Customers will identify ‘red’ means ‘product X’ without reading the label. (Examples attached and below we believe do this well).

Current 30ml bottle, cap, and dropper are in black and will remain so. Current label is black, however, we have a white label on our local product (example attached) and prefer the look of it.

Packaging is currently black and could remain so however most products that appeal to our target market are in white with color accents.

One consideration we have is that the product up until now has been selling exceptionally well so we need to retain some kind of familiarity with the existing branding. Perhaps that’s just the logo.

Logo can be revised i.e. add company name and/or company slogan.

Products are: (Function - Name)

Testosterone Support - Tongkat Ali (current)
Hormone Support - Jiaogulan
Energy Support - Ashwaghanda
Libido Support - Krachai Dam (for men)
Libido Support - Kacip Fatimah (for women)
Sleep Support - Wild Chamomile

Packaging: 4.6cm (L) x 8.0cm (W) x 11.2cm (H)
Label: 30 mL bottle

https://www.portfolioshelf.example/gallery/TONIC-BOX-STUDY-2012/8824160
http://www.pelrostudio.example/projects/#/harbor-tea/
https://www.portfolioshelf.example/gallery/57730482/Velmora-Skin
https://au.pinboardly.example/pin/913402775610238841/
https://au.pinboardly.example/pin/61470329814550298/
http://kelvo.studio.example/en/portfolio/logo-redesign/

Target Market(s)

Generation X Men (and their partners), 36-55, upper middle class, who appreciate quality products.

Industry/Entity Type

Health Product

Font styles to use
Serif
Sans Serif

Requirements
Must have
• Packaging - Principal Display Panel (Front):
• 1. Function & Name of each product i.e 'Testosterone Support' & 'Tongkat Ali'
• 2. '30ml' AND '1 fl oz' (text size 1.8in / 3.2mm / 9 point min.)
• 3. 'Dietary Supplement'
• Packaging - Information Panel (Right):
• 1. Supplement Facts Panel (template accepted for drafts)
• 2. Directions: (lorum ipsum accepted for drafts)
• 3. Safety Warning: (lorum ipsum accepted for drafts)
• 4. 'Manufactured for: Copperfield Vitals LLC'
• 5. 'Sheridan, Wyoming'
• 6. '(307) 641 3528'
• 7. 'Product of Thailand'
• Bottle Label:
• 3. 'Dietary Supplement'
• 4. Supplement Facts Panel (template accepted for drafts)
• 5. Directions: (lorum ipsum accepted for drafts)
• 6. Safety Warning: (forum ipsum accepted for drafts)
• 7. 'Manufactured for: Copperfield Vitals LLC'
• 8. 'Sheridan, Wyoming'
• 9. '(307) 641 3528'
• 10. 'Product of Thailand'
Nice to have
• Updated logo with company name 'Copperfield Vitals' and/or company slogan 'Quality Without Compromise' added.
Should not have
• No photos or stock images.
• No elements of the current design (excluding logo) to remain i.e. 'Otter Finn', 'Testosterone Booster', 'Increase Lean Muscle', 'Stabilise Hormones', 'Boost Endurance', 'Improve Muscle Naturally', are all to be omitted.

```html
<!DOCTYPE html>
<html lang="en">
<head>
<meta charset="utf-8">
<title>Copperfield Vitals – Testosterone Support Carton</title>
<link rel="stylesheet" href="https://fonts.googleapis.com/css2?family=Share+Tech+Mono&family=Roboto+Condensed:wght@400;700&display=swap">
<style>
  :root {
    --brand-red: #c01e2b;
    --brand-red-deep: #a81a25;
    --ink: #1c1c1c;
    --paper: #ffffff;
    --backdrop: #e9e9e9;
    --rule: #3a3a3a;
  }
  * { box-sizing: border-box; margin: 0; padding: 0; }
  html, body { width: 960px; height: 1200px; overflow: hidden; }
  body {
    background: radial-gradient(ellipse at 50% 45%, #fafafa 0%, var(--backdrop) 100%);
    font-family: "Share Tech Mono", monospace;
    position: relative;
  }
  .carton { position: absolute; left: 86px; top: 106px; width: 788px; height: 988px; }

  /* Top flap */
  .panel-top {
    position: absolute; left: 288px; top: 0; width: 500px; height: 288px;
    background: linear-gradient(135deg, var(--brand-red) 0%, var(--brand-red-deep) 100%);
    display: flex; align-items: center; justify-content: center;
  }
  .panel-top .brand-lockup { color: var(--paper); }

  /* Information panel */
  .panel-side {
    position: absolute; left: 0; top: 288px; width: 288px; height: 700px;
    background: linear-gradient(90deg, var(--brand-red) 0%, var(--brand-red-deep) 100%);
    color: var(--paper);
    padding: 34px 26px;
  }
  .info-heading { font-size: 16px; font-weight: 400; letter-spacing: 2px; margin-bottom: 8px; text-transform: uppercase; }
  .info-copy { font-family: "Roboto Condensed", sans-serif; font-size: 12.5px; line-height: 1.45; }
  .info-block { margin-bottom: 22px; }

  .facts {
    background: var(--paper); color: var(--ink);
    border: 1px solid var(--ink); padding: 8px 10px;
    font-family: "Roboto Condensed", sans-serif; font-size: 10.5px;
    margin-bottom: 150px;
  }
  .facts-title { font-size: 22px; font-weight: 700; line-height: 1; }
  .facts-serving { border-bottom: 6px solid var(--ink); padding: 3px 0 4px; }
  .facts-table { width: 100%; border-collapse: collapse; }
  .facts-table th { font-weight: 700; text-align: right; padding: 2px 0; border-bottom: 3px solid var(--ink); }
  .facts-table th:first-child { text-align: left; }
  .facts-table td { padding: 2px 0; border-bottom: 1px solid var(--ink); text-align: right; }
  .facts-table td:first-child { text-align: left; }
  .facts-table td.indent { padding-left: 10px; }
  .facts-foot { border-top: 6px solid var(--ink); margin-top: 2px; padding-top: 3px; font-size: 9.5px; line-height: 1.3; }

  /* Principal display panel */
  .panel-front {
    position: absolute; left: 288px; top: 288px; width: 500px; height: 700px;
    background: var(--paper);
    display: flex; flex-direction: column; align-items: center;
    padding-top: 120px;
  }
  .brand-lockup {
    display: flex; align-items: center; gap: 12px;
    font-family: "Share Tech Mono", monospace; font-size: 28px; letter-spacing: 2px;
    color: var(--brand-red); text-transform: uppercase;
  }
  .brand-dot { width: 20px; height: 20px; border-radius: 50%; background: currentColor; }

  .product-function {
    margin-top: 140px; text-align: center; font-weight: 400;
    color: var(--brand-red); font-size: 44px; letter-spacing: 7px; line-height: 1.15;
  }
  .product-name-band { margin-top: 34px; width: 356px; }
  .product-name-band .rule { display: block; width: 100%; height: 3px; }
  .product-name {
    text-align: center; font-size: 26px; letter-spacing: 6px; color: var(--ink);
    padding: 14px 0;
  }
  .net-content { margin-top: 62px; font-size: 26px; letter-spacing: 2px; color: var(--ink); }
  .product-type { margin-top: 12px; font-size: 18px; letter-spacing: 4px; color: var(--ink); }
</style>
</head>
<body>
  <main class="carton">
    <section class="panel-top" aria-label="Top flap">
      <div class="brand-lockup"><span class="brand-dot"></span>Copperfield Vitals</div>
    </section>

    <section class="panel-side" aria-label="Information panel">
      <div class="info-block">
        <h2 class="info-heading">Directions:</h2>
        <p class="info-copy">Lorem ipsum dolor sit amet, consectetuer adipiscing elit, sed diam nonummy nibh euismod tincidunt ut laoreet dolore magna aliquam erat volutpat.</p>
      </div>

      <div class="facts">
        <div class="facts-title">Supplement Facts</div>
        <div class="facts-serving">Serving Size 1 Lozenge</div>
        <table class="facts-table">
          <tr><th>Amount Per Serving</th><th></th><th>% Daily Value</th></tr>
          <tr><td>Total Carbohydrate</td><td>1 g</td><td>&lt;1%*</td></tr>
          <tr><td class="indent">Sugars</td><td>1 g</td><td>†</td></tr>
          <tr><td>Vitamin C</td><td>50 mg</td><td>80%</td></tr>
          <tr><td>Zinc (as zinc citrate)</td><td>5 mg</td><td>33%</td></tr>
          <tr><td>Sodium</td><td>7 mg</td><td>†</td></tr>
          <tr><td>Herbal extract blend</td><td>5 mg</td><td>†</td></tr>
        </table>
        <div class="facts-foot">* Percent Daily Values are based on a 2,000 calorie diet.<br>† Daily Value not established.</div>
      </div>

      <div class="info-block">
        <h2 class="info-heading">Safety Warning:</h2>
        <p class="info-copy">Lorem ipsum dolor sit amet, consectetuer adipiscing elit, sed diam nonummy nibh euismod tincidunt ut laoreet dolore magna aliquam erat volutpat.</p>
      </div>
      <h2 class="info-heading">Storage:</h2>
    </section>

    <section class="panel-front" aria-label="Principal display panel">
      <div class="brand-lockup"><span class="brand-dot"></span>Copperfield Vitals</div>

      <h1 class="product-function">TESTOSTERONE<br>SUPPORT</h1>

      <div class="product-name-band">
        <svg class="rule" viewBox="0 0 356 3" preserveAspectRatio="none" aria-hidden="true">
          <polygon points="0,1.5 178,0 356,1.5 178,3" fill="var(--rule)"/>
        </svg>
        <div class="product-name">TONGKAT ALI</div>
        <svg class="rule" viewBox="0 0 356 3" preserveAspectRatio="none" aria-hidden="true">
          <polygon points="0,1.5 178,0 356,1.5 178,3" fill="var(--rule)"/>
        </svg>
      </div>

      <div class="net-content">30ML</div>
      <div class="product-type">DIETARY SUPPLEMENT</div>
    </section>
  </main>
</body>
</html>
```